Menu for burgers the restaurant will be called 'THE BLUEJAY'

something special that reflects the image of a relaxed and friendly bar.
you will find a picture of a menu for inspiration.
Some examples uploaded

Target Market(s)

all categories who search for simple and funny bar for watching football

Requirements
Must have
• some funny emoticons
font style - like the picture of the menu uploaded
if you can do the same menu it will be perfect !!! the cow at the background etc...
Nice to have
• black font style and colorful wall (not too much) simple and elegant
Should not have
• a lot of colours
serious emoticons

```html
<!DOCTYPE html>
<html lang="fr">
<head>
<meta charset="utf-8">
<title>The Bluejay – Menu</title>
<link rel="stylesheet" href="https://fonts.googleapis.com/css2?family=Bebas+Neue&family=Oswald:wght@500;600&family=Roboto+Condensed:wght@400;700&display=swap">
<style>
:root{
  --bg:#ffffff;
  --paper:#e4d8b9;
  --paper-edge:#c9b78f;
  --ink:#1b1a18;
  --cream:#f1e9d3;
}
*{box-sizing:border-box;margin:0;padding:0}
html,body{width:1200px;height:1200px;overflow:hidden;background:var(--bg)}
.menu-sheet{
  position:absolute;left:20px;top:190px;width:836px;height:590px;
  transform:scale(1.3876);transform-origin:0 0;
  background:radial-gradient(ellipse at 50% 50%,var(--cream) 0%,var(--paper) 55%,var(--paper-edge) 100%);
  color:var(--ink);font-family:"Oswald",sans-serif;
}
.abs{position:absolute}
.v-title{position:absolute;writing-mode:vertical-rl;transform:rotate(180deg);
  font-family:"Bebas Neue",sans-serif;line-height:1;white-space:nowrap;text-align:center}
.section-title{font-size:33px;letter-spacing:1px}
.tbl{position:absolute;border:1px solid var(--ink)}
.tbl-head{display:grid;grid-template-columns:1fr 30px 30px;height:15px;font-size:9px;font-family:"Roboto Condensed",sans-serif;text-align:center}
.tbl-head span{border-left:1px solid var(--ink);border-bottom:1px solid var(--ink);line-height:14px}
.tbl-head span:first-child{border:none}
.item{border-top:1px solid var(--ink)}
.tbl-head + .item{border-top:none}
.item-line{display:grid;grid-template-columns:1fr 30px 30px;align-items:stretch}
.item-line.wide{grid-template-columns:1fr 33px 35px}
.item-name{font-family:"Bebas Neue",sans-serif;font-size:17px;line-height:17px;padding:2px 3px 0;white-space:nowrap}
.item-name small{font-size:11px}
.price{border-left:1px solid var(--ink);border-bottom:1px solid var(--ink);font-family:"Bebas Neue",sans-serif;font-size:15px;text-align:center;line-height:19px}
.item-desc{font-family:"Roboto Condensed",sans-serif;font-weight:700;font-size:5.2px;line-height:6.6px;text-transform:uppercase;padding:3px 3px 4px;letter-spacing:.1px}
.icon-block{position:absolute;background:var(--ink);border-radius:3px}
.leaf-icon{display:inline-block;vertical-align:middle;width:16px;height:11px;margin-left:4px;background:var(--ink);border-radius:8px 0}
.sub-title{position:absolute;font-family:"Bebas Neue",sans-serif;font-size:20px;text-align:center;width:155px}
.list{position:absolute;border:1px solid var(--ink)}
.list-row{display:grid;grid-template-columns:1fr 38px;font-family:"Roboto Condensed",sans-serif;font-weight:700;font-size:7px;text-transform:uppercase;border-top:1px solid var(--ink)}
.list-row:first-child{border-top:none}
.list-row span{padding:3px 4px;line-height:13px}
.list-row b{border-left:1px solid var(--ink);font-family:"Bebas Neue",sans-serif;font-weight:400;font-size:13px;text-align:center;line-height:19px}
.note{position:absolute;font-family:"Roboto Condensed",sans-serif;font-weight:700;font-size:5.5px;text-transform:uppercase;text-align:center}
.brand{left:448px;top:20px;font-size:44px;letter-spacing:1px;height:198px}
.hours-box{position:absolute;left:507px;top:20px;width:54px;height:165px;border:1px solid var(--ink)}
.hours-box .v-title{font-size:17px;line-height:18px;left:6px;top:8px;height:148px;text-align:left}
.bubble{position:absolute;left:540px;top:255px;width:58px;height:58px;border-radius:50%;background:var(--ink);color:var(--cream);
  font-family:"Bebas Neue",sans-serif;font-size:12px;line-height:13px;text-align:center;padding-top:16px}
.bubble::after{content:"";position:absolute;left:4px;bottom:-4px;border:7px solid transparent;border-top-color:var(--ink);transform:rotate(35deg)}
.stars{position:absolute;left:458px;top:356px;width:196px;font-size:10px;letter-spacing:3.2px;white-space:nowrap;overflow:hidden}
.small-name{font-family:"Bebas Neue",sans-serif;font-size:16px;line-height:19px;padding-left:4px}
.halal{position:absolute;left:243px;top:548px;width:155px;text-align:center;font-family:"Bebas Neue",sans-serif;font-size:17px}
</style>
</head>
<body>
<div class="menu-sheet">

  <!-- BEEF -->
  <div class="v-title section-title" style="left:28px;top:20px;height:226px">Burgers Bœuf</div>
  <div class="tbl" style="left:68px;top:20px;width:150px">
    <div class="tbl-head"><span></span><span>B</span><span>M</span></div>
    <div class="item"><div class="item-line"><div class="item-name">Big Beef</div><div class="price">8.9</div><div class="price">13.9</div></div>
      <div class="item-desc">Ketchup, cornichons, oignons caramélisés, tomate, salade, sauce maison</div></div>
    <div class="item"><div class="item-line"><div class="item-name">Big Cheese</div><div class="price">10.9</div><div class="price">15.9</div></div>
      <div class="item-desc">Cheddar, ketchup, cornichons, oignons caramélisés, tomate, salade, sauce maison</div></div>
    <div class="item"><div class="item-line"><div class="item-name">Mexicana Beef</div><div class="price">12.9</div><div class="price">17.9</div></div>
      <div class="item-desc">Guacamole, ketchup, oignons caramélisés, salade, tomate, sauce maison</div></div>
    <div class="item"><div class="item-line"><div class="item-name"><small>THE</small>Special One</div><div class="price">12.9</div><div class="price">17.9</div></div>
      <div class="item-desc">Purée de tomate maison, œuf, huile d'olive, persil, sauce maison</div></div>
    <div class="item"><div class="item-line"><div class="item-name">Red Hot Chili<br>Burger</div><div class="price">12.9</div><div class="price">17.9</div></div>
      <div class="item-desc">Cheddar, oignons caramélisés, tomate, salade, sauce piquante maison</div></div>
  </div>
  <div class="icon-block" role="img" aria-label="Petite silhouette de vache" style="left:76px;top:6px;width:34px;height:26px"></div>

  <div class="tbl" style="left:243px;top:20px;width:155px">
    <div class="tbl-head" style="grid-template-columns:1fr 33px 35px"><span></span><span>B</span><span>M</span></div>
    <div class="item"><div class="item-line wide"><div class="item-name">Die Schweizer</div><div class="price">12.9</div><div class="price">17.9</div></div>
      <div class="item-desc">Fromage à raclette aux poivres, cornichons, salade, oignons caramélisés, sauce moutarde</div></div>
    <div class="item"><div class="item-line wide"><div class="item-name">The Goat</div><div class="price">13.9</div><div class="price">18.9</div></div>
      <div class="item-desc">Bacon, rondelle de chèvre, miel, oignons caramélisés, salade, sauce maison</div></div>
    <div class="item"><div class="item-line wide"><div class="item-name">El Matador</div><div class="price">12.9</div><div class="price">17.9</div></div>
      <div class="item-desc">Chorizo, jalapeños, tomate, salade, sauce aïoli maison</div></div>
    <div class="item"><div class="item-line wide"><div class="item-name">Smokey Beef</div><div class="price">12.9</div><div class="price">17.9</div></div>
      <div class="item-desc">Bacon, cheddar, oignons caramélisés, onion rings, salade, sauce BBQ</div></div>
  </div>
  <div class="icon-block" role="img" aria-label="Petite silhouette de vache" style="left:252px;top:6px;width:34px;height:26px"></div>

  <svg class="abs" style="left:275px;top:262px" width="78" height="32" viewBox="0 0 78 32" aria-hidden="true">
    <g fill="var(--ink)"><polygon points="0,0 12,0 22,16 12,32 0,32 10,16"/><polygon points="18,0 30,0 40,16 30,32 18,32 28,16"/><polygon points="36,0 48,0 58,16 48,32 36,32 46,16"/><polygon points="54,0 66,0 76,16 66,32 54,32 64,16"/></g>
  </svg>

  <div class="sub-title" style="left:243px;top:316px">Suppléments viandes</div>
  <div class="list" style="left:243px;top:343px;width:155px">
    <div class="list-row"><span>Bœuf (160g)</span><b>4.5</b></div>
    <div class="list-row"><span>Poulet (120g)</span><b>4</b></div>
  </div>
  <div class="sub-title" style="left:243px;top:388px">Toppings</div>
  <div class="list" style="left:243px;top:414px;width:155px">
    <div class="list-row"><span style="line-height:7px">Fromage, œuf, bacon, chorizo, guacamole, oignons caramélisés</span><b>2</b></div>
  </div>
  <div class="sub-title" style="left:243px;top:445px">Upgrades</div>
  <div class="list" style="left:243px;top:472px;width:155px">
    <div class="list-row"><span>Potatoes</span><b>+2</b></div>
    <div class="list-row"><span>Milkshake classique</span><b>+3</b></div>
    <div class="list-row"><span>Bière</span><b>+3</b></div>
  </div>
  <div class="halal">Halal sur demande</div>

  <!-- CHICKEN -->
  <div class="v-title section-title" style="left:2px;top:326px;height:246px">Burgers Poulet</div>
  <div class="tbl" style="left:68px;top:320px;width:150px">
    <div class="tbl-head"><span></span><span>B</span><span>M</span></div>
    <div class="item"><div class="item-line"><div class="item-name">The Crispy</div><div class="price">8.9</div><div class="price">13.9</div></div>
      <div class="item-desc">Cheddar, ketchup, cornichons, oignons caramélisés, tomate, salade, sauce maison</div></div>
    <div class="item"><div class="item-line"><div class="item-name">Mexicana<br>Chicken</div><div class="price">12.9</div><div class="price">17.9</div></div>
      <div class="item-desc">Cheddar, ketchup, cornichons, oignons caramélisés, tomate, salade, sauce maison</div></div>
    <div class="item"><div class="item-line"><div class="item-name">Grecos</div><div class="price">8.9</div><div class="price">13.9</div></div>
      <div class="item-desc">Cheddar, ketchup, cornichons, oignons caramélisés, tomate, salade, sauce maison</div></div>
    <div class="item"><div class="item-line"><div class="item-name">Burger<br>Veggie<span class="leaf-icon" role="img" aria-label="Petite feuille"></span></div><div class="price">12.9</div><div class="price">17.9</div></div>
      <div class="item-desc">Cheddar, ketchup, oignons caramélisés, tomate, salade, sauce maison</div></div>
  </div>
  <div class="icon-block" role="img" aria-label="Petite silhouette de poule" style="left:76px;top:306px;width:24px;height:26px"></div>
  <div class="icon-block" role="img" aria-label="Petite feuille" style="left:122px;top:314px;width:18px;height:12px;border-radius:9px 0"></div>

  <!-- CENTER -->
  <div class="v-title brand">The Bluejay</div>
  <div class="hours-box"><div class="v-title">Opening hours:&nbsp;&nbsp;Also:<br>17:00 – 23:00&nbsp;&nbsp;To take away</div></div>
  <div class="abs" role="img" aria-label="Gravure d'une tête de taureau" style="left:446px;top:232px;width:92px;height:106px;border-radius:40% 40% 45% 45%;background:radial-gradient(ellipse at 50% 45%,#a69a80 0%,#5e574b 60%,rgba(60,55,48,0) 100%)"></div>
  <div class="bubble">B = Burger<br>M = Menu</div>

  <!-- COMPETITION -->
  <div class="icon-block" role="img" aria-label="Petite moustache" style="left:604px;top:20px;width:34px;height:9px;border-radius:6px"></div>
  <div class="v-title" style="left:600px;top:36px;height:180px;font-size:22px;line-height:20px">Competition Burgers<br><span style="font-size:14px">Demandez les 'avant 20min'</span></div>
  <div class="tbl" style="left:660px;top:20px;width:158px">
    <div class="item"><div class="item-line" style="grid-template-columns:1fr 36px"><div class="item-name">The Monster<br>'Big Mouth Burger'</div><div class="price" style="line-height:34px">39.9</div></div>
      <div class="item-desc" style="border-bottom:1px solid var(--ink);font-size:7px">Si fini en 15 min -&gt; dessert offert</div>
      <div class="item-desc">Triple beef, triple cheddar, cornichons, salade, tomate, sauce maison, double ration de frites et boisson</div></div>
    <div class="item"><div class="item-line" style="grid-template-columns:1fr 36px"><div class="item-name">Moving Mountain<br>Burger</div><div class="price" style="line-height:34px">69.9</div></div>
      <div class="item-desc" style="border-bottom:1px solid var(--ink);font-size:7px">Si fini en 20 min -&gt; chicha offerte</div>
      <div class="item-desc">Quintuple beef, quintuple cheddar, cornichons, onion rings, salade, tomate, sauce maison, frites cheddar et boisson</div></div>
  </div>

  <!-- SALADS -->
  <div class="icon-block" role="img" aria-label="Petit ornement en feuilles" style="left:630px;top:240px;width:14px;height:12px;border-radius:50%"></div>
  <div class="v-title section-title" style="left:620px;top:258px;height:84px;font-size:26px">Salades</div>
  <div class="tbl" style="left:660px;top:240px;width:158px">
    <div class="item"><div class="item-line" style="grid-template-columns:1fr 36px"><div class="item-name">Chicken Salad</div><div class="price">16.9</div></div>
      <div class="item-desc">Filet de poulet, salade, tomate, gruyère AOP, onion rings, sauce au citron vert</div></div>
    <div class="item"><div class="item-line" style="grid-template-columns:1fr 36px"><div class="item-name">Hawaii</div><div class="price">17.9</div></div>
      <div class="item-desc">Crevettes roses, ananas, avocats, concombre, coriandre, feuilles de salade, sauce cocktails</div></div>
  </div>

  <div class="stars">★★★★★★★★★★★★★★★★★★★★★★★★★★★★</div>

  <!-- STUDENT -->
  <div class="v-title" style="left:456px;top:378px;height:122px;font-size:22px">Menu étudiant</div>
  <div class="list" style="left:487px;top:380px;width:135px">
    <div class="list-row"><span class="small-name">Big Beef</span><b>11.9</b></div>
    <div class="list-row"><span class="small-name">Big Cheese</span><b>12.9</b></div>
    <div class="list-row"><span class="small-name">The Crispy</span><b>12.9</b></div>
    <div class="list-row"><span class="small-name">The Veggie</span><b>12.9</b></div>
  </div>
  <div class="note" style="left:487px;top:461px;width:135px">(avec boisson sans alcool et frites)<br>un menu par carte d'étudiant</div>

  <!-- KIDS -->
  <div class="v-title" style="left:624px;top:378px;height:124px;font-size:22px">Menu enfant</div>
  <div class="tbl" style="left:660px;top:358px;width:158px">
    <div class="tbl-head"><span></span><span>B</span><span>M</span></div>
    <div class="item"><div class="item-line"><div class="small-name">Junior Beef</div><div class="price">6.9</div><div class="price">10.9</div></div></div>
    <div class="item"><div class="item-line"><div class="small-name">Junior Cheese</div><div class="price">7.9</div><div class="price">11.9</div></div></div>
    <div class="item"><div class="item-line"><div class="small-name">Junior Crispy</div><div class="price">7.9</div><div class="price">11.9</div></div></div>
    <div class="item"><div class="item-line"><div class="small-name">Junior Veggie</div><div class="price">7.9</div><div class="price">11.9</div></div></div>
  </div>
  <div class="note" style="left:660px;top:463px;width:158px">(avec boisson sans alcool et frites)</div>

  <!-- SIDES -->
  <svg class="abs" style="left:456px;top:518px" width="24" height="22" viewBox="0 0 24 22" aria-hidden="true">
    <polygon points="5,1 19,1 23,7 12,21 1,7" fill="none" stroke="var(--ink)" stroke-width="1.6"/>
    <polyline points="1,7 23,7" fill="none" stroke="var(--ink)" stroke-width="1.2"/>
  </svg>
  <div class="list" style="left:488px;top:510px;width:167px">
    <div class="list-row"><span>Patatas bravas</span><b>8.9</b></div>
    <div class="list-row"><span>Filets de poulets 'tenders'</span><b>12.9</b></div>
    <div class="list-row"><span>Beef chili cheese fries</span><b>14.9</b></div>
  </div>
  <div class="list" style="left:660px;top:510px;width:158px">
    <div class="list-row"><span>Onion rings (4 pièces)</span><b>4.9</b></div>
    <div class="list-row"><span>Frites</span><b>4.9</b></div>
    <div class="list-row"><span>Potatoes</span><b>5.9</b></div>
  </div>

</div>
</body>
</html>
```